We need our website look and feel updated to match our brand

We are looking to update our website and a "where to buy" tab at the top of the website. The current look and feel is ok but needs a clean up. The task is as follows:
1. Update the current pages and add a page for "Where to Buy"
2. Update the product page to reflect our current products. ie we have only three products now. Undercoat Q, Undercoat R and VELMIST. This page will have very similar descriptions and at the bottom of each product will be a link to our SDS (safety data sheets).
3. Please visit our current website for the look and feel.
4. Use our New Taglines need to be included. "Always Cleaning. All the Time." "24/7 SAFE SURFACE PROTECTION" (Logo as well)
5. The HomePage will need a nice clean location to our corporate video. https://clipvanta.com/Rk3TpWq9ZxN (link for viewing) that will be the highlight and easy to access on the homepage.
Some examples of websites we like.
https://lumivera.com/
https://orvastrell.com/ (like the use of motion graphics in these)
Our focus claims are that our product is a surface cleaner and deodorizer. We would like to see variations in black, white background (Black header bar) and Gray backgrounds.
5+ page

```html
<!DOCTYPE html>
<html lang="en">
<head>
<meta charset="utf-8">
<title>Lumacoat – Always Cleaning. All the Time.</title>
<link href="https://fonts.googleapis.com/css2?family=Poppins:wght@400;500;600;700;800&display=swap" rel="stylesheet">
<style>
:root{
  --yellow:#ffc907;
  --black:#000;
  --ink:#0d0d0d;
  --card:#1a1a1a;
  --white:#fff;
  --muted:#cfcfcf;
  --line:#6b6b6b;
}
*{box-sizing:border-box;margin:0;padding:0}
html,body{width:1200px;height:4412px;overflow:hidden;background:var(--ink)}
body{font-family:'Poppins',sans-serif;color:var(--white)}
.page{position:relative;width:1200px;height:4412px;overflow:hidden;
  background:linear-gradient(180deg,#000 0,#000 870px,#111 1000px,#141414 1600px,#2a2a2a 2250px,#1c1c1c 2500px,#111 3000px,#121212 3950px,#222 4412px)}
.abs{position:absolute}
.btn{position:absolute;background:var(--yellow);color:#000;font-weight:700;font-size:15px;display:flex;align-items:center;justify-content:center;letter-spacing:.2px}
.logo{position:absolute;display:flex;align-items:center;gap:12px}
.logo-mark{width:22px;height:22px;background:var(--yellow)}
.logo-name{font-weight:600;font-size:42px;color:var(--white);letter-spacing:-.5px}
/* header */
.contact-box{position:absolute;border-left:2px solid var(--yellow);border-top:2px solid var(--yellow);border-bottom:2px solid var(--yellow);padding:8px 0 0 14px;height:58px}
.contact-box b{display:block;color:var(--yellow);font-size:12px;font-weight:700}
.contact-box span{font-size:10px;color:var(--white)}
.navbar{position:absolute;left:0;top:133px;width:1200px;height:58px;background:var(--yellow);display:flex;align-items:center;padding-left:100px}
.navbar a{color:#000;font-size:12px;font-weight:700;text-decoration:none}
.navbar .sep{margin:0 28px;font-weight:600;color:#000;font-size:13px}
/* hero */
.hero-photo{position:absolute;left:640px;top:191px;width:560px;height:677px;
  background:radial-gradient(ellipse at 70% 25%,#e9e9e9 0,#9a9a9a 18%,#3a3a3a 40%,transparent 62%),radial-gradient(ellipse at 25% 45%,rgba(200,200,200,.35) 0,transparent 45%)}
.hero-frame{position:absolute;left:135px;top:295px;width:160px;height:385px;border:5px solid var(--yellow);border-right:none}
.hero-frame::before,.hero-frame::after{content:"";position:absolute;right:-5px;width:5px;height:40px;background:var(--yellow)}
.hero-frame::before{top:-5px}.hero-frame::after{bottom:-5px}
.hero-title{position:absolute;left:183px;top:345px;font-size:62px;font-weight:800;line-height:76px}
.hero-title em{font-style:normal;color:var(--yellow)}
.hero-sub{position:absolute;left:183px;top:508px;font-size:25px;font-weight:700}
.slides{position:absolute;left:38px;top:448px}
.slides i{display:block;width:9px;height:9px;margin-bottom:8px;background:var(--yellow)}
.slides i:first-child{background:var(--white)}
.slides span{position:absolute;left:18px;top:13px;font-size:10px;white-space:nowrap}
.video{position:absolute;left:225px;top:737px;width:750px;height:375px;background:linear-gradient(180deg,#7c8a96 0,#a7a58b 40%,#b9a640 75%,#c5ae35 100%)}
.play{position:absolute;left:352px;top:165px;width:46px;height:46px}
/* headings */
.h2{position:absolute;left:0;width:1200px;text-align:center;font-size:36px;font-weight:800}
.h2 em,.ph em{font-style:normal;color:var(--yellow)}
.copy{position:absolute;left:200px;width:800px;text-align:center;font-size:13px;line-height:24px;color:var(--white)}
/* products */
.card{position:absolute;top:1745px;width:305px;height:420px;background:var(--card);text-align:center}
.bottle{position:absolute;left:96px;top:45px;width:113px;height:222px;border-radius:30px 30px 22px 22px}
.card h3{position:absolute;top:298px;left:0;width:100%;font-size:21px;font-weight:700}
.price{position:absolute;top:340px;left:0;width:100%;font-size:15px}
.price s{margin-right:16px}
.stars{position:absolute;top:368px;left:0;width:100%;font-size:11px;color:var(--yellow);letter-spacing:1px}
/* projects */
.ph{position:absolute;font-size:36px;font-weight:800}
.pinfo{position:absolute;font-size:13px;line-height:16px;width:490px}
.pinfo p{margin-bottom:16px}
.frame{position:absolute;border:7px solid var(--yellow)}
.photo{position:absolute}
/* footer */
.follow{position:absolute;left:345px;top:4110px;color:var(--yellow);font-weight:700;font-size:22px;letter-spacing:1px}
.social{position:absolute;top:4158px;width:22px;height:22px;border:2px solid var(--muted);border-radius:50%}
.signup{position:absolute;left:574px;top:4122px;width:489px;height:61px;border:2px solid var(--white);display:flex}
.signup .field{flex:1;background:#1d1d1d;color:var(--white);font-size:16px;display:flex;align-items:center;padding-left:32px}
.signup .go{width:195px;background:var(--yellow);color:#000;font-weight:700;font-size:15px;display:flex;align-items:center;justify-content:center;gap:36px}
.fnav{position:absolute;left:0;top:4238px;width:1200px;display:flex;justify-content:center;font-size:16px;font-weight:600}
.fnav .sep{margin:0 22px}
.rule{position:absolute;left:88px;top:4294px;width:975px;height:1px;background:#888}
.legal{position:absolute;left:0;top:4340px;width:1200px;text-align:center;font-size:16px;color:#bdbdbd}
</style>
</head>
<body>
<div class="page">

  <!-- header -->
  <div class="logo" style="left:100px;top:40px"><div class="logo-mark"></div><div class="logo-name">Lumacoat</div></div>
  <div class="contact-box" style="left:567px;top:40px;width:100px"><b>CALL US</b><span>+1 555 010 4420</span></div>
  <div class="contact-box" style="left:750px;top:40px;width:140px"><b>EMAIL US</b><span>hello@lumacoat.com</span></div>
  <div class="btn" style="left:933px;top:49px;width:166px;height:44px;font-size:15px">WHERE TO BUY</div>

  <nav class="navbar">
    <a>HOME</a><span class="sep">|</span><a>ABOUT US</a><span class="sep">|</span><a>WHERE TO BUY</a><span class="sep">|</span><a>OUR TECHNOLOGY</a><span class="sep">|</span><a>NEWS</a><span class="sep">|</span><a>FAQ</a><span class="sep">|</span><a>CONTACT US</a>
    <svg class="abs" style="left:1030px;top:20px" width="18" height="18" viewBox="0 0 18 18" fill="none" stroke="#000" stroke-width="1.8"><circle cx="7.5" cy="7.5" r="6"/><path d="M12 12l5 5"/></svg>
    <svg class="abs" style="left:1078px;top:19px" width="20" height="20" viewBox="0 0 20 20" fill="none" stroke="#000" stroke-width="1.6"><circle cx="10" cy="10" r="8.5"/><circle cx="10" cy="8" r="3"/><path d="M4.5 16c1.5-3 9.5-3 11 0"/></svg>
  </nav>

  <!-- hero -->
  <div class="hero-photo" role="img" aria-label="Hand holding a spray gun releasing a fine mist"></div>
  <div class="slides"><i></i><i></i><i></i><i></i><span>— 02</span></div>
  <div class="hero-frame"></div>
  <h1 class="hero-title">Always Cleaning.<br><em>All the Time.</em></h1>
  <div class="hero-sub">24/7 SAFE SURFACE PROTECTION.</div>
  <div class="btn" style="left:183px;top:575px;width:157px;height:41px;font-size:17px">SHOP NOW</div>

  <div class="video" role="img" aria-label="Corporate video preview: illustrated cleaning crew spraying a room">
    <svg class="play" viewBox="0 0 46 46"><circle cx="23" cy="23" r="20" fill="rgba(0,0,0,.25)" stroke="#fff" stroke-width="3"/><path d="M18 14l13 9-13 9z" fill="#fff"/></svg>
  </div>

  <!-- real world solution -->
  <h2 class="h2" style="top:1183px">REAL WORLD <em>SOLUTION</em></h2>
  <p class="copy" style="top:1257px">The onset of COVID-19 has changed our lives forever. The current methods of cleaning surfaces are not sustainable. Cleaning the environment we live in with caustic UV-C light, ammonia-based cleaners and other harsh chemicals is wasteful. The moment you clean the surface and an infected person touches that surface again, it requires reapplication of your protective cleaners.</p>
  <p class="copy" style="top:1377px">Lumacoat is bringing a permanent surface coating formula to the United States market. A titanium dioxide photocatalyst coating that is incredibly long lasting and durable. How long? It basically lasts as long as the substrate is present. As long as it's not mechanically removed or painted over, Lumacoat lasts for decades on any surface, indoor or outdoor.</p>
  <div class="btn" style="left:532px;top:1482px;width:137px;height:41px">READ MORE</div>

  <!-- products -->
  <h2 class="h2" style="top:1664px">OUR <em>PRODUCTS</em></h2>
  <div class="card" style="left:113px">
    <div class="bottle" role="img" aria-label="Undercoat Q gallon jug" style="background:linear-gradient(180deg,#f2f2f2,#d8d8d8)"></div>
    <h3>UNDERCOAT Q</h3><div class="price"><s>$ 45.00</s>$ 30.00</div><div class="stars">★★★★☆</div>
  </div>
  <div class="card" style="left:448px">
    <div class="bottle" role="img" aria-label="Undercoat R gallon jug" style="background:linear-gradient(180deg,#f6e3b0,#e8b35c)"></div>
    <h3>UNDERCOAT R</h3><div class="price"><s>$ 45.00</s>$ 30.00</div><div class="stars">★★★★☆</div>
  </div>
  <div class="card" style="left:782px">
    <div class="bottle" role="img" aria-label="Velmist gallon jug" style="background:linear-gradient(180deg,#f7ecb6,#e9cd5a)"></div>
    <h3>VELMIST</h3><div class="price"><s>$ 45.00</s>$ 30.00</div><div class="stars">★★★★☆</div>
  </div>

  <!-- projects -->
  <h2 class="h2" style="top:2366px">OUR <em>PROJECTS</em></h2>

  <h3 class="ph" style="left:113px;top:2525px">UNIVERSITY <em>HOSPITAL</em></h3>
  <div class="pinfo" style="left:113px;top:2594px">
    <p>Project Description: Constant Cleaning and santizing of operating room<br>Home : Inside the Hospital of Eastbay University Medical School<br>Construction day : 01/20/2008</p>
    <p>weather : Interior with low humidity<br>Construction content : Ward Room 1、2 Interior Construction</p>
    <p>Material Used: Lumacoat UV-A Coating</p>
    <p>Construction Area : 70㎡ x 2</p>
    <p>Purpose : antibacterial, deodorant</p>
  </div>
  <div class="btn" style="left:113px;top:2826px;width:137px;height:41px">READ MORE</div>
  <div class="frame" style="left:770px;top:2522px;width:314px;height:352px"></div>
  <div class="photo" role="img" aria-label="Hospital operating room lit in blue" style="left:660px;top:2552px;width:397px;height:292px;background:linear-gradient(160deg,#9be8ff,#2fb4e8 55%,#1b6fa3)"></div>

  <div class="frame" style="left:113px;top:2982px;width:306px;height:350px"></div>
  <div class="photo" role="img" aria-label="Clean residential bathroom with tub and vanity" style="left:138px;top:3012px;width:390px;height:288px;background:linear-gradient(150deg,#b9b3ad,#8d8781 50%,#e8e6e3)"></div>
  <h3 class="ph" style="left:614px;top:2985px">ODORLESS <em>BATHROOMS</em></h3>
  <div class="pinfo" style="left:614px;top:3054px;width:470px">
    <p>Client Name: Norvale SA men's, women's, multipurpose and sub toilets project<br>Site Address: Harrowfield City, Westmere Prefecture<br>The Problem: Bathroom smells elimination without the use of harsh chemicals and constant cleaning</p>
    <p>The Solution: Lumacoat Visible Light Coating</p>
    <p>Application Process: Lumacoat was applied using a conventional automotive spray gun. Coating was applied in three layers for maximum coverage</p>
  </div>
  <div class="btn" style="left:614px;top:3267px;width:138px;height:42px">READ MORE</div>

  <h3 class="ph" style="left:113px;top:3457px">BURGERHAUS <em>VOLCANO</em></h3>
  <div class="pinfo" style="left:113px;top:3527px">
    <p>Project Description: Constant cleaning of exterior.<br>Site Address : 12-4 Orinmachi, Sendale City, Sendale Prefecture<br>Construction day : 09/18/2013</p>
    <p>weather : Clear and sunny</p>
    <p>Construction site : Painted exterior walls and glass surfaces</p>
    <p>construction method : Lumacoat CA/CG Glass method<br>Objective : Exterior constant cleaning</p>
  </div>
  <div class="btn" style="left:113px;top:3742px;width:139px;height:41px">READ MORE</div>
  <div class="frame" style="left:770px;top:3452px;width:318px;height:364px"></div>
  <div class="photo" role="img" aria-label="Fast food restaurant exterior with red and yellow signage" style="left:658px;top:3483px;width:405px;height:310px;background:linear-gradient(90deg,#c9c3b4 0,#e2c96a 45%,#c8231d 60%,#b81e1a 100%)"></div>

  <!-- footer -->
  <div class="logo" style="left:110px;top:4124px"><div class="logo-mark"></div><div class="logo-name" style="font-size:38px">Lumacoat</div></div>
  <div class="follow">FOLLOW US</div>
  <div class="social" style="left:347px"></div>
  <div class="social" style="left:398px"></div>
  <div class="signup">
    <div class="field">Email Address</div>
    <div class="go">SIGN UP
      <svg width="24" height="22" viewBox="0 0 24 22" fill="none" stroke="#000" stroke-width="1.6"><path d="M1 10L23 1 17 21 11 13z"/><path d="M11 13L23 1"/></svg>
    </div>
  </div>
  <div class="fnav">
    <span>HOME</span><span class="sep">|</span><span>ABOUT US</span><span class="sep">|</span><span>WHERE TO BUY</span><span class="sep">|</span><span>OUR TECHNOLOGY</span><span class="sep">|</span><span>NEWS</span><span class="sep">|</span><span>FAQ</span><span class="sep">|</span><span>CONTACT US</span>
  </div>
  <div class="rule"></div>
  <div class="legal">Copyright © 2021 Lumacoat |Privacy Policy | Terms &amp; Consitions . All Rights Reserved.</div>
</div>
</body>
</html>
```